| 希望する色 | オレンジ系 追記事項: 希望としていますが、サイトをご確認頂き、合う色味があればそちらで作成頂き問題ありません。 |
| 弊社で運営しております、ソラテックというサービスに掲載する、購買意欲向上の為、 訴求バナーを掲載したいと考えております。 また、ABテストや、ケース別で掲載を変更したく、今回は3件の募集をさせて頂きます。 サイト自体は青系の色を基調とし構築されております。 https://soratecku-web.jp/shop-item.html 【訴求文言】 導線ではなく、購入を促進させる目的である為、以下の文言を挿入、強調をお願いします。 --------------------------- ・90日間保証 ・全国送料無料 ・メーカー純正キー ・年間1万本の作成実績 ・簡単1分注文 ---------------------------- |
キーワードの使用方法、デザインのバランスもとてもよく、
かつ、わかりやすい印象がありましたので、1案目として採用をさせて頂きます。
皆様からの沢山のご提案、ありがとうございました。
どの案も素晴らしく、弊社内でも採用に関して意見が分かれる程でした。
また、機会がありましたら皆様からご応募頂けますと幸いです。

```html
<!DOCTYPE html>
<html lang="ja">
<head>
<meta charset="UTF-8">
<title>ソラテック 純正キー注文バナー</title>
<link href="https://fonts.googleapis.com/css2?family=Noto+Sans+JP:wght@700;900&display=swap" rel="stylesheet">
<style>
  :root {
    --ribbon-red: #b8392a;
    --ribbon-shade: #7e2318;
    --headline-orange: #f28a16;
    --headline-edge: #6b3208;
    --badge-blue: #1f76c4;
    --logo-ink: #2f6fb5;
    --bg-warm: #fbf6ee;
    --bg-white: #ffffff;
    --frame: #dcd6cc;
    --key-silver-light: #eef0f2;
    --key-silver-dark: #a9adb3;
  }
  html, body {
    margin: 0;
    padding: 0;
    overflow: hidden;
    background: var(--bg-white);
  }
  .banner {
    position: relative;
    width: 1200px;
    height: 278px;
    box-sizing: border-box;
    border: 2px solid var(--frame);
    background: linear-gradient(90deg, var(--bg-warm) 0%, var(--bg-white) 60%);
    font-family: "Noto Sans JP", sans-serif;
    overflow: hidden;
  }
  .track-record {
    position: absolute;
    left: 8px;
    top: 8px;
    width: 540px;
    height: 62px;
  }
  .track-record svg {
    position: absolute;
    inset: 0;
  }
  .track-record span {
    position: absolute;
    left: 30px;
    top: 0;
    line-height: 56px;
    white-space: nowrap;
    color: #fff;
    font-weight: 700;
    font-size: 32px;
    letter-spacing: 2px;
  }
  .headline {
    position: absolute;
    left: 18px;
    top: 86px;
    margin: 0;
    white-space: nowrap;
    font-weight: 900;
    color: var(--headline-orange);
    -webkit-text-stroke: 2px var(--headline-edge);
    paint-order: stroke fill;
    text-shadow: 2px 3px 0 rgba(107, 50, 8, 0.35);
    line-height: 1;
  }
  .headline .line-one {
    display: block;
    font-size: 68px;
    letter-spacing: 1px;
  }
  .headline .line-two {
    display: block;
    margin-top: 16px;
    font-size: 76px;
    letter-spacing: 10px;
  }
  .product-visual {
    position: absolute;
    left: 670px;
    top: 10px;
    width: 260px;
    height: 258px;
    border-radius: 40px 40px 8px 8px;
    background: linear-gradient(160deg, var(--key-silver-light) 0%, var(--key-silver-dark) 100%);
    opacity: 0.85;
  }
  .benefits {
    position: absolute;
    left: 958px;
    top: 20px;
    width: 222px;
    display: flex;
    flex-direction: column;
    gap: 14px;
  }
  .benefit {
    height: 44px;
    border-radius: 6px;
    background: var(--badge-blue);
    color: #fff;
    font-weight: 700;
    font-size: 27px;
    white-space: nowrap;
    display: flex;
    align-items: center;
    justify-content: center;
    letter-spacing: 2px;
  }
  .brand {
    position: absolute;
    left: 966px;
    top: 146px;
    display: flex;
    align-items: center;
    gap: 10px;
    white-space: nowrap;
    font-weight: 900;
    font-size: 38px;
    color: var(--logo-ink);
  }
  .brand .dot {
    width: 20px;
    height: 20px;
    border-radius: 50%;
    background: var(--logo-ink);
  }
</style>
</head>
<body>
  <div class="banner">
    <div class="track-record">
      <svg width="540" height="62" viewBox="0 0 540 62" aria-hidden="true">
        <polygon points="0,0 540,0 520,28 540,56 0,56" fill="var(--ribbon-red)"/>
        <polygon points="0,56 14,56 14,62" fill="var(--ribbon-shade)"/>
      </svg>
      <span>年間１万本の作成実績</span>
    </div>

    <h1 class="headline">
      <span class="line-one">メーカー純正キーが</span>
      <span class="line-two">簡単１分注文</span>
    </h1>

    <div class="product-visual" role="img" aria-label="メーカー純正の銀色の合鍵2本"></div>

    <div class="benefits">
      <div class="benefit">９０日間保証</div>
      <div class="benefit">全国送料無料</div>
    </div>

    <div class="brand">
      <span class="brand-name">ソラテック</span>
      <span class="dot" aria-hidden="true"></span>
    </div>
  </div>
</body>
</html>
```